Velmora Design

Looking for Velmora banner and square design:
Velmora Banner
W:1600 px H:400 px
Square
120x120

Logo attached.

Description: Data-Driven stock market portfolio management using quantitative analysis.

```html
<!DOCTYPE html>
<html lang="en">
<head>
<meta charset="utf-8">
<title>Velmora Banner and Square</title>
<link rel="stylesheet" href="https://fonts.googleapis.com/css2?family=Montserrat:wght@300;400;600;800&display=swap">
<style>
  :root {
    --page: #e6e7e9;
    --paper: #f6f6f8;
    --paper-white: #ffffff;
    --ghost-chart: #efeff2;
    --brand-blue: #0a6fb8;
    --deep-blue: #0d4f84;
    --sky-blue: #0a8ae2;
    --text-grey: #2d3a47;
  }
  * { box-sizing: border-box; margin: 0; padding: 0; }
  html, body {
    width: 1200px;
    height: 568px;
    overflow: hidden;
    background: var(--page);
    font-family: "Montserrat", sans-serif;
  }
  .canvas { position: relative; width: 1200px; height: 568px; }
  .banner {
    position: absolute;
    left: 61px;
    top: 140px;
    width: 1078px;
    height: 270px;
    background: linear-gradient(90deg, var(--paper-white), var(--paper));
    overflow: hidden;
    box-shadow: 0 6px 10px rgba(0,0,0,0.12);
  }
  .banner-art { position: absolute; inset: 0; width: 1078px; height: 270px; }
  .brand-lockup {
    position: absolute;
    left: 36px;
    top: 110px;
    height: 34px;
    display: flex;
    align-items: center;
    gap: 10px;
  }
  .brand-dot { width: 30px; height: 30px; border-radius: 50%; background: var(--brand-blue); }
  .brand-name {
    font-weight: 600;
    font-size: 26px;
    line-height: 1;
    color: var(--brand-blue);
    white-space: nowrap;
  }
  .headline {
    position: absolute;
    left: 112px;
    top: 50px;
    width: 600px;
    text-align: center;
    white-space: nowrap;
  }
  .headline-main {
    display: block;
    font-weight: 800;
    font-size: 46px;
    line-height: 50px;
    letter-spacing: 1px;
    color: var(--brand-blue);
  }
  .headline-sub {
    display: block;
    margin-top: -2px;
    font-weight: 300;
    font-size: 33px;
    line-height: 36px;
    letter-spacing: 0.5px;
    color: var(--deep-blue);
  }
  .features {
    position: absolute;
    left: 112px;
    top: 152px;
    width: 600px;
    list-style: none;
    text-align: center;
    font-weight: 300;
    font-size: 16px;
    line-height: 19px;
    color: var(--text-grey);
    white-space: nowrap;
  }
  .features li + li { margin-top: 7px; }
  .illustration {
    position: absolute;
    left: 700px;
    top: 8px;
    width: 370px;
    height: 262px;
    border-radius: 18px;
    background: radial-gradient(ellipse at 55% 55%, rgba(255,255,255,0.6), rgba(210,230,250,0.25) 55%, rgba(255,255,255,0) 75%);
  }
  .square-tile {
    position: absolute;
    left: 567px;
    top: 367px;
    width: 86px;
    height: 86px;
    border: 2px solid var(--paper-white);
    background: linear-gradient(135deg, var(--brand-blue), var(--deep-blue));
    display: flex;
    align-items: center;
    justify-content: center;
    box-shadow: 0 5px 8px rgba(0,0,0,0.18);
  }
  .square-name { font-weight: 600; font-size: 15px; color: var(--paper-white); }
</style>
</head>
<body>
<main class="canvas">
  <section class="banner">
    <svg class="banner-art" viewBox="0 0 1078 270" aria-hidden="true">
      <path class="ghost-area-chart" fill="var(--ghost-chart)"
        d="M0,200 C40,170 90,110 130,60 C160,25 180,25 210,60 C250,105 270,110 300,75 C340,30 370,35 400,65 C430,95 460,85 490,35 C515,0 535,0 565,40 C600,95 640,90 680,60 L660,270 L0,270 Z"/>
      <path class="sky-blob" fill="var(--sky-blue)"
        d="M727,0 H1078 V270 H617 C617,205 660,155 720,138 C765,125 772,105 748,78 C725,52 720,22 727,0 Z"/>
    </svg>

    <div class="brand-lockup">
      <span class="brand-dot"></span>
      <span class="brand-name">Velmora</span>
    </div>

    <h1 class="headline">
      <span class="headline-main">DATA-DRIVEN</span>
      <span class="headline-sub">STOCK MARKET</span>
    </h1>

    <ul class="features">
      <li>RULES-BASED STOCK PORTFOLIO</li>
      <li>MONTHLY STOCK ROTATION<br>STRATEGY USING FACTOR ANALYSIS</li>
    </ul>

    <div class="illustration" role="img" aria-label="Isometric illustration of analysts on floating platforms around dashboard screens with charts and data servers"></div>
  </section>

  <div class="square-tile">
    <span class="square-name">Velmora</span>
  </div>
</main>
</body>
</html>
```